energy rating company

Web Design graphics and layout only

To create two pages for the website. First the home page and the second is the design for the job board for our clients use after login. I have attached files that explain in detail what the pages should have and the purpose/desires of each object. Please read these thoroughly.

The webpages need to be clean, professional, easy on the eye, obvious in all its buttons and functions with a strong call to action on the home page and branding and clean, great and obvious looking buttons and very simple but dynamic as well. We wish to be seen as contemporary.

Business Concept

Our business concept is simple, to build a website whereby our clients will be able to upload jobs for energy raters to quote on and subsequent complete the work if their quote is selected. To link energy ratings that are required with energy raters via our website. Similarly to the varn website, jobs will be “advertised” on the job board and raters will select which jobs they wish to quote for.

I have attached a Word document explaining all the parts of the website and another word document showing what we are sort of after and a excel spreadsheet as well. Please read these in conjunction with this brief!
Updates

Dear All

I have submitted with my brief a word doc and excel spreadsheet of the two pages I want created.  However this is not the layout or design I want, I only put it together so that you will need to know what is required on each page.  Feel free to change and redesign it all.

Also the second page does not require the "process" logo or any other menu items except the first five being Home, How it works, About Us, testimonials and Contact us as per the home page.

We also are looking for something very professional and very clean.  It should be very easy to see exactly what you are looking for.

I will also extend the deadline for new designers!!  I am excited to see your talents!!

Thanks

I have increase budget and posted a note saying feel free to change all the details layout etc on my brief just include everything!!! 

Wanting a professional corporate look...

Want a professional corporate look

We have changed our minds and you we no longer require the process to be on the home page.

Thanks

Target Market(s)

Target Market

Home Inspection Companies
Pest Inspection Companies
Residential home buyers/sellers
Real Estate companies

Industry/Entity Type

It Company

Number of Pages Required

1 page

Requirements
Must have
• Colours and Styles

• The website should be mainly white as I believe it is seen as clean and simple with colour from the logos, but can be swayed if it projects the image we are after.

• It should be obvious and process orientated and I do believe symbols, pictures, etc should replace words where possible.

```html
<!DOCTYPE html>
<html lang="en">
<head>
<meta charset="utf-8">
<title>Tarvenby Rating – Home</title>
<link href="https://fonts.googleapis.com/css2?family=Ropa+Sans&family=Noto+Sans:ital@0;1&family=Arimo:wght@400;700&display=swap" rel="stylesheet">
<style>
:root{
  --orange:#b9521a;
  --orange-light:#f2b48c;
  --green:#1f9a45;
  --grey-text:#555;
  --grey-light:#cfcfcf;
  --body:#222;
  --band:#f1f1f1;
  --gold:#f6c24a;
}
*{box-sizing:border-box;margin:0;padding:0}
html,body{width:1200px;height:960px;overflow:hidden;background:#fff}
body{position:relative;font-family:"Noto Sans",sans-serif;color:var(--body)}
.header{position:absolute;left:0;top:0;width:1200px;height:197px;background:linear-gradient(#fff 60%,var(--band))}
.brand{position:absolute;left:110px;top:118px;display:flex;align-items:center;gap:10px;font-family:"Ropa Sans",sans-serif;font-size:34px;color:var(--orange)}
.brand-dot{width:26px;height:26px;border-radius:50%;background:var(--gold)}
.nav{position:absolute;top:28px;right:105px;display:flex;gap:38px;font-family:"Ropa Sans",sans-serif;font-size:16px;color:var(--grey-text)}
.nav a{color:inherit;text-decoration:none;position:relative;padding-bottom:10px}
.nav a::after{content:"";position:absolute;left:50%;bottom:0;margin-left:-3px;border:3px solid transparent;border-bottom:4px solid #e07a2c}
.nav a.active{color:var(--green);padding-top:12px;padding-bottom:0}
.nav a.active::after{top:0;bottom:auto;border-bottom:0;border-top:4px solid #e07a2c}
.quick{position:absolute;top:98px;display:flex;align-items:center;gap:14px;font-family:"Ropa Sans",sans-serif;color:#444}
.quick .art{width:76px;height:72px;border-radius:10px}
.quick strong{font-weight:400;font-size:19px;display:block}
.quick span{font-size:15px}
.steps{position:absolute;left:0;top:220px;width:1200px;height:200px}
.step{position:absolute;top:0;width:190px}
.step .art{position:absolute;top:4px;left:40px;width:108px;height:94px;border-radius:14px}
.step svg{position:absolute;top:113px;left:0}
.step p{position:absolute;top:131px;left:0;width:175px;text-align:center;font-family:"Ropa Sans",sans-serif;font-size:20px;line-height:26px}
.step.warm p{color:var(--orange)}
.step.cool p{color:#444}
.intro{position:absolute;left:107px;top:458px;width:692px;font-size:12px;line-height:15px;letter-spacing:.55px}
.intro p{margin-bottom:14px}
.intro .lead{font-weight:700;font-size:12.5px;letter-spacing:.4px}
.benefits{list-style:none;margin:0 0 15px;font-style:italic}
.benefits li{position:relative;padding-left:33px;line-height:14.8px}
.benefits li svg{position:absolute;left:12px;top:2px}
.card{position:absolute;left:838px;width:259px;background:linear-gradient(#fff,#fafafa);border-radius:10px;box-shadow:0 1px 3px rgba(0,0,0,.35)}
.login{top:454px;height:154px;padding:12px 20px}
.login h2{font-family:"Arimo",sans-serif;font-size:22px;color:var(--orange);margin-bottom:8px}
.login h2 span{color:var(--green)}
.login input{display:block;width:221px;height:25px;margin-bottom:8px;border:1px solid #c8c8c8;padding:0 7px;font-family:"Noto Sans",sans-serif;font-size:13px;color:#333}
.login input::placeholder{color:#333}
.login button{position:absolute;right:20px;top:112px;width:83px;height:23px;border:1px solid #8a3d12;background:linear-gradient(#d9782e,#b3521b);color:#fff;font-family:"Arimo",sans-serif;font-weight:700;font-size:15px}
.quote{top:636px;height:142px;padding:30px 20px 0}
.quote blockquote{font-family:"Arimo",sans-serif;font-size:14px;line-height:17px;color:#333}
.quote time{display:block;margin-top:6px;font-family:"Arimo",sans-serif;font-size:12px;color:var(--orange)}
.quote::after{content:"";position:absolute;left:190px;bottom:-16px;border:12px solid transparent;border-top:16px solid #fafafa;filter:drop-shadow(0 1px 1px rgba(0,0,0,.25))}
.author{position:absolute;right:104px;top:800px;font-family:"Arimo",sans-serif;font-size:15px;color:#333}
.author b{color:var(--green)}
.footer{position:absolute;left:0;top:852px;width:1200px;height:108px;background:linear-gradient(var(--band),#fff 70%)}
.footer small{position:absolute;left:108px;top:30px;font-family:"Noto Sans",sans-serif;font-size:12px;line-height:16px;color:#333}
.footer-brand{position:absolute;right:104px;top:30px;display:flex;align-items:center;gap:12px;font-family:"Ropa Sans",sans-serif;font-size:36px;color:#a9a9a9}
.footer-brand i{width:60px;height:60px;border-radius:50%;background:#c4c4c4}
</style>
</head>
<body>
<header class="header">
  <div class="brand"><i class="brand-dot"></i>Tarvenby Rating</div>
  <nav class="nav">
    <a class="active" href="#">Home</a><a href="#">How it works?</a><a href="#">About Us</a><a href="#">Testimonials</a><a href="#">Contact Us</a>
  </nav>
  <a class="quick" style="left:426px"><div class="art" role="img" aria-label="Speech bubble with pencil" style="background:radial-gradient(#e8f6fb,#9fd1e6)"></div><strong>Get a quote</strong></a>
  <a class="quick" style="left:642px"><div class="art" role="img" aria-label="Rising green bar chart with red arrow" style="background:linear-gradient(135deg,#f3f3f3,#7cc46a)"></div><div><strong>Energy Raters</strong><span>Add your busines</span></div></a>
  <a class="quick" style="left:876px"><div class="art" role="img" aria-label="Spreadsheet job board" style="background:linear-gradient(#f7f9fc,#d5dbe5)"></div><strong>Active Job Board</strong></a>
</header>

<section class="steps">
  <div class="step warm" style="left:112px"><div class="art" role="img" aria-label="Notebook and pencil" style="background:linear-gradient(135deg,#f7f0d8,#f1b83b)"></div>
    <svg width="190" height="85"><defs><linearGradient id="warm" x1="0" x2="1"><stop offset="0" stop-color="#fff"/><stop offset="1" stop-color="#f2b48c"/></linearGradient><linearGradient id="cool" x1="0" x2="1"><stop offset="0" stop-color="#fff"/><stop offset="1" stop-color="#c8c8c8"/></linearGradient></defs><path d="M0 0H155L190 42 155 85H0Z" fill="url(#warm)"/></svg><p>Post a<br>Job</p></div>
  <div class="step cool" style="left:317px"><div class="art" role="img" aria-label="Orange quotes speech bubble" style="background:linear-gradient(#fbe08a,#f0a83a)"></div>
    <svg width="190" height="85"><path d="M0 0H155L190 42 155 85H0Z" fill="url(#cool)"/></svg><p>Get As many<br>Quotes as you like</p></div>
  <div class="step warm" style="left:518px"><div class="art" role="img" aria-label="Circular energy arrows" style="background:radial-gradient(#e6e43a,#c8641c)"></div>
    <svg width="190" height="85"><path d="M0 0H155L190 42 155 85H0Z" fill="url(#warm)"/></svg><p>Select Energy<br>Quote that suits</p></div>
  <div class="step cool" style="left:708px"><div class="art" role="img" aria-label="Gold coins and banknotes" style="background:linear-gradient(#f3d27a,#b38a2e)"></div>
    <svg width="190" height="85"><path d="M0 0H155L190 42 155 85H0Z" fill="url(#cool)"/></svg><p>Approve<br>Payment</p></div>
  <div class="step warm" style="left:907px"><div class="art" role="img" aria-label="Gold star" style="background:radial-gradient(#fde36a,#f09a1c)"></div>
    <svg width="190" height="85"><path d="M0 0H155L190 42 155 85H0Z" fill="url(#warm)"/></svg><p>Receive<br>Rating</p></div>
</section>

<main class="intro">
  <p>Tarvenby Rating is Australia’s leading professional energy rating consultancy firm specializing in large scaled residential and commercial energy rating logistics.</p>
  <p>We have professional and accredited energy raters in all States and Territories ready and waiting to provide quotes for and perform&nbsp; your energy rating jobs!</p>
  <p class="lead">It’s Free, Fast and Easy to use and you get the best price and turnaround time that suits you!!</p>
  <p>Register with us, upload your job and specifications, and sit back and watch as energy raters provide quotes for your work!</p>
  <ul class="benefits">
    <li><svg width="12" height="10"><path d="M1 5l3.5 3.5L11 1" fill="none" stroke="#3a9a2e" stroke-width="2.2"/></svg>Get the best priced quotes for your energy ratings</li>
    <li><svg width="12" height="10"><path d="M1 5l3.5 3.5L11 1" fill="none" stroke="#3a9a2e" stroke-width="2.2"/></svg>Save time by listing a job to get many quotes</li>
    <li><svg width="12" height="10"><path d="M1 5l3.5 3.5L11 1" fill="none" stroke="#3a9a2e" stroke-width="2.2"/></svg>Monitor your jobs and quotes on your own job board</li>
    <li><svg width="12" height="10"><path d="M1 5l3.5 3.5L11 1" fill="none" stroke="#3a9a2e" stroke-width="2.2"/></svg>Be notified via email of all new quotes as they come in</li>
    <li><svg width="12" height="10"><path d="M1 5l3.5 3.5L11 1" fill="none" stroke="#3a9a2e" stroke-width="2.2"/></svg>Be able to specify your desired turnaround times</li>
    <li><svg width="12" height="10"><path d="M1 5l3.5 3.5L11 1" fill="none" stroke="#3a9a2e" stroke-width="2.2"/></svg>Accessible anytime and anywhere</li>
    <li><svg width="12" height="10"><path d="M1 5l3.5 3.5L11 1" fill="none" stroke="#3a9a2e" stroke-width="2.2"/></svg>Choose a deadline for energy raters to supply quotes</li>
    <li><svg width="12" height="10"><path d="M1 5l3.5 3.5L11 1" fill="none" stroke="#3a9a2e" stroke-width="2.2"/></svg>Have access to many qualified energy raters in your state all quoting for your work</li>
    <li><svg width="12" height="10"><path d="M1 5l3.5 3.5L11 1" fill="none" stroke="#3a9a2e" stroke-width="2.2"/></svg>Be able to track your jobs and pay online</li>
    <li><svg width="12" height="10"><path d="M1 5l3.5 3.5L11 1" fill="none" stroke="#3a9a2e" stroke-width="2.2"/></svg>Provide feedback on energy raters</li>
  </ul>
  <p>Its totally free to be registered with us and there is no obligations or hidden catches!&nbsp; So if you wish to utilise the amazing opportunity register now!&nbsp; This new website will be going live on the (insert date) so be ready to save some money!</p>
</main>

<form class="card login">
  <h2>User <span>Login</span></h2>
  <input type="text" placeholder="Username">
  <input type="password" placeholder="Password">
  <button type="button">LOGIN</button>
</form>

<aside class="card quote">
  <blockquote>"Lorem ipsum dolor sit amet, consectetur adipisicing elit, sed do eiusmod tempor incididu"</blockquote>
  <time>03.03.2010 10:30:00</time>
</aside>
<p class="author"><b>Marten</b>, manager</p>

<footer class="footer">
  <small>Copyright 2010 (C) www.tarvenbyrating.example<br>Allrights reserved</small>
  <div class="footer-brand"><i></i>Tarvenby Rating</div>
</footer>
</body>
</html>
```